Shadeway Loft Shop Direct Mail Card

I am looking to get a postcard 5.5 X 8.5; that communicates that we provide free in-home consultations and installations. If they call today they will get a promotional discount up to $250 off their order (when they order 7+ of any window coverings).

Keypoints:
Free In-Home Consultation (valued $159)
Free Installation & Removal (Old Blinds)
Experienced & Trained Installers
Fast Turnaround
Courtesy (temporary shades)

Target Market(s)

Homeowners

Industry/Entity Type

Retail

Font styles to use
Sans Serif

Colors
9bcb3c
0492cd
474747

Requirements
Must have
• Clear call to action: "Call or visit us online for your Free In-Home Consultation"
• Free In-Home Consultation (valued $159)
• Free Installation & Removal (Old Blinds)
• Experienced & Trained Installers
• Fast Turnaround
• Courtesy (temporary shades)
• Back Of Post Card:
• $250 Gift Certificate (See Attached Example)
Nice to have
• Modern look with bold fonts
Should not have
• Old school designs

```html
<!DOCTYPE html>
<html lang="en">
<head>
<meta charset="utf-8">
<title>Shadeway Loft Shop Direct Mail Card</title>
<link rel="stylesheet" href="https://fonts.googleapis.com/css2?family=Comfortaa:wght@700&family=Varela+Round&family=Montserrat:wght@400;500;700&family=PT+Sans+Narrow&display=swap">
<style>
  :root {
    --brown: #28150f;
    --green: #a0b83f;
    --white: #ffffff;
    --stage: #777777;
    --rule: #d6d6d6;
  }
  * { box-sizing: border-box; margin: 0; padding: 0; }
  html, body { width: 1200px; height: 1174px; overflow: hidden; background: var(--stage); }
  .postcard {
    position: absolute; left: 175px; width: 850px; height: 550px;
    background: var(--white); overflow: hidden;
  }
  .postcard--front { top: 30px; }
  .postcard--back { top: 600px; }

  /* Front */
  .cta-band { position: absolute; left: 30px; top: 34px; width: 480px; height: 90px; }
  .cta-band svg { position: absolute; inset: 0; }
  .cta-title {
    position: absolute; left: 20px; top: 10px;
    font: 700 36px/1 "Comfortaa", sans-serif; color: var(--green); white-space: nowrap;
  }
  .cta-sub {
    position: absolute; left: 19px; top: 52px;
    font: 700 20px/1 "Comfortaa", sans-serif; color: var(--white); white-space: nowrap;
  }
  .brand-front {
    position: absolute; left: 490px; top: 48px; width: 330px; text-align: center;
    font: 700 30px/1.2 "Comfortaa", sans-serif; color: var(--brown); white-space: nowrap;
  }
  .photo { position: absolute; top: 129px; height: 184px; width: 255px; }
  .photo--kitchen { left: 30px; background: linear-gradient(160deg, #e9e6e1 0%, #bfb8ae 55%, #4a3b30 100%); }
  .photo--shutters { left: 296px; background: linear-gradient(180deg, #cfd0cc 0%, #8d8f88 55%, #3a3634 100%); }
  .photo--door { left: 558px; background: linear-gradient(90deg, #8a5a2e 0%, #c99a62 40%, #e2c8a2 70%, #9c7448 100%); }

  .benefits {
    position: absolute; left: 30px; top: 318px; width: 519px; height: 214px;
    background: var(--green); border: 1px solid #6f7f2a; padding: 20px 0 0 14px;
  }
  .benefits ul { list-style: none; }
  .benefits li {
    font: 21px/34.5px "Varela Round", sans-serif; color: var(--brown); letter-spacing: 0.5px;
  }
  .benefits li::before { content: "•"; display: inline-block; width: 18px; font-size: 16px; }
  .benefits strong { font-family: "Montserrat", sans-serif; font-weight: 700; font-size: 19px; }

  .offer {
    position: absolute; left: 559px; top: 318px; width: 254px; height: 214px;
    background: var(--brown); text-align: center; color: var(--green);
  }
  .offer-lead { margin-top: 18px; font: 700 21px/26px "Comfortaa", sans-serif; }
  .offer-amount { font: 700 44px/44px "Comfortaa", sans-serif; margin-top: 2px; }
  .offer-tail { font: 700 21px/24px "Comfortaa", sans-serif; }
  .offer-note { margin-top: 14px; font: 15px/1 "PT Sans Narrow", sans-serif; color: var(--white); }

  /* Back */
  .gift-panel { position: absolute; left: 0; top: 0; width: 425px; height: 550px; background: var(--green); }
  .gift-panel svg { position: absolute; inset: 0; }
  .gift-copy { position: absolute; left: 0; top: 58px; width: 415px; text-align: center; color: var(--white); }
  .gift-kicker { font: 400 20px/1 "Montserrat", sans-serif; }
  .gift-amount { font: 700 84px/1 "Montserrat", sans-serif; color: var(--green); margin-top: 4px; letter-spacing: -2px; }
  .gift-label { font: 500 26px/1 "Montserrat", sans-serif; margin-top: 6px; }
  .brand-back {
    position: absolute; left: 40px; top: 410px; width: 345px; text-align: center;
    font: 700 32px/1 "Montserrat", sans-serif; color: var(--brown); white-space: nowrap;
  }
  .stamp { position: absolute; left: 704px; top: 37px; width: 94px; height: 94px; border: 1px solid var(--rule); }
  .address-to { position: absolute; left: 483px; top: 224px; font: 400 15px/1 "Montserrat", sans-serif; color: var(--brown); }
  .address-line { position: absolute; left: 499px; width: 289px; border-top: 1px solid var(--rule); }
</style>
</head>
<body>

<section class="postcard postcard--front">
  <div class="cta-band">
    <svg width="480" height="90" viewBox="0 0 480 90" aria-hidden="true">
      <path d="M0 0 H470 C440 20 420 55 416 90 H0 Z" fill="var(--brown)"/>
    </svg>
    <div class="cta-title">Call or visit us online</div>
    <div class="cta-sub">for your Free In-Home Consultation</div>
  </div>
  <div class="brand-front">Shadeway Loft Shop</div>

  <div class="photo photo--kitchen" role="img" aria-label="Bright white kitchen with island and patio door"></div>
  <div class="photo photo--shutters" role="img" aria-label="Living room windows fitted with white shutters"></div>
  <div class="photo photo--door" role="img" aria-label="Patio doors with wooden blinds"></div>

  <div class="benefits">
    <ul>
      <li>Free In-Home Consultation <strong>(valued $159)</strong></li>
      <li>Free Installation &amp; Removal <strong>(Old Blinds)</strong></li>
      <li>Experienced &amp; Trained Installers</li>
      <li>Fast Turnaround</li>
      <li>Courtesy (Temporary shades)</li>
    </ul>
  </div>

  <div class="offer">
    <p class="offer-lead">Call today &amp; get<br>a promotional<br>discount up to</p>
    <p class="offer-amount">$250</p>
    <p class="offer-tail">off your order*</p>
    <p class="offer-note">*(Order 7+ of any window coverings).</p>
  </div>
</section>

<section class="postcard postcard--back">
  <div class="gift-panel">
    <svg width="425" height="550" viewBox="0 0 425 550" aria-hidden="true">
      <path d="M0 0 H425 V316 C250 312 70 270 0 160 Z" fill="var(--brown)"/>
    </svg>
    <div class="gift-copy">
      <p class="gift-kicker">A GIFT FOR YOU</p>
      <p class="gift-amount">$250</p>
      <p class="gift-label">GIFT CERTIFICATE</p>
    </div>
    <div class="brand-back">Shadeway Loft Shop</div>
  </div>

  <div class="stamp"></div>
  <p class="address-to">To</p>
  <div class="address-line" style="top:297px"></div>
  <div class="address-line" style="top:343px"></div>
  <div class="address-line" style="top:384px"></div>
  <div class="address-line" style="top:431px"></div>
</section>

</body>
</html>
```